Rack card for a integrative medical practice

Need an eye-catching rack card with our logo with content as provided. We have a membership based holistic medical practice which incorporates western and holistic medicine. We would like to focus on wellness and healthy lifestyle. See uploaded files for what is included in the membership. Would like 2 page rack card color on both sides. Logo must be on the front.

Target Market(s)

People looking for alternative medicine, healthy lifestyle.

Industry/Entity Type

Health and Wellness

Colors
00AB8E
00BBA5
67D7C9
C6EFE9
E9F9F6

Requirements
Must have
• Must spark interest at first sight. Clear message.
Nice to have
• Warm, bright and positive vibe. Organic, neutral and earthy colors.
Should not have
• Traditional medical practice vibe (cold, formal, industrial). No PINK except the logo.

```html
<!DOCTYPE html>
<html lang="en">
<head>
<meta charset="utf-8">
<title>Sorrel Health &amp; Wellness – Rack Card</title>
<link href="https://fonts.googleapis.com/css2?family=Roboto+Condensed:wght@300;400;700&display=swap" rel="stylesheet">
<style>
  :root{
    --backdrop:#f8c6dc;
    --cream:#f3e9df;
    --mint:#dff4ef;
    --mint-soft:#c6efe9;
    --teal:#00ab8e;
    --teal-bright:#00bba5;
    --logo-pink:#e02a82;
    --forest:#17382b;
    --ink:#1d2a24;
    --grey:#4f5a57;
    --white:#ffffff;
  }
  *{box-sizing:border-box;margin:0;padding:0}
  html,body{width:1200px;height:1082px;overflow:hidden}
  body{background:var(--backdrop);position:relative;font-family:"Roboto Condensed",Arial,sans-serif}
  .card{position:absolute;top:85px;width:405px;height:912px;overflow:hidden;box-shadow:0 14px 22px rgba(0,0,0,.28)}
  .card--front{left:166px;background:var(--cream)}
  .card--back{left:640px;background:var(--mint)}

  /* front */
  .brand{position:absolute;top:26px;left:0;width:100%;text-align:center;color:var(--forest);z-index:2}
  .brand__mark{width:60px;height:60px;border-radius:50%;background:var(--logo-pink);margin:0 auto 10px}
  .brand__name{font-weight:400;font-size:50px;letter-spacing:9px;line-height:1}
  .brand__tag{font-weight:400;font-size:12px;letter-spacing:5px;margin-top:4px}
  .hero{position:absolute;left:0;top:120px;width:405px;height:540px}
  .headline{position:absolute;top:652px;left:0;width:100%;text-align:center;color:var(--forest);font-weight:700;line-height:1.05}
  .headline__main{font-size:32px}
  .headline__sub{font-size:24px}
  .phone{position:absolute;left:43px;top:760px;width:316px;height:60px;border-radius:30px;background:var(--teal);color:var(--white);display:flex;align-items:center;gap:10px;padding-left:12px;font-size:40px;font-weight:400}
  .phone__icon{width:40px;height:40px;border-radius:50%;background:var(--white);display:flex;align-items:center;justify-content:center;flex:none}
  .address{position:absolute;top:834px;left:0;width:100%;text-align:center;font-size:17px;color:var(--ink)}

  /* back */
  .back-top{position:absolute;left:0;top:0;width:405px;height:180px}
  .back-title{position:absolute;top:33px;left:50px;display:flex;align-items:center;gap:12px;color:var(--teal);font-weight:700;font-size:25px;line-height:1.08}
  .back-title__mark{width:50px;height:50px;border-radius:50%;background:var(--logo-pink);flex:none}
  .perks{position:absolute;top:192px;left:46px;list-style:none}
  .perk{display:flex;align-items:flex-start;gap:16px;margin-bottom:12px;color:var(--grey);font-weight:300;font-size:20px;line-height:1.28}
  .perk__icon{width:40px;height:40px;border-radius:50%;background:var(--teal);flex:none;display:flex;align-items:center;justify-content:center;margin-top:4px}
  .card--back .phone{top:760px}
  .website{position:absolute;top:830px;left:0;width:100%;text-align:center;font-size:34px;letter-spacing:4px;color:var(--ink);font-weight:300}
  .website strong{font-weight:700}
</style>
</head>
<body>

<article class="card card--front">
  <svg class="hero" viewBox="0 0 405 540">
    <defs>
      <linearGradient id="heroFill" x1="0" y1="0" x2="1" y2="1">
        <stop offset="0" stop-color="#8a9a62"/>
        <stop offset=".45" stop-color="#b06a72"/>
        <stop offset="1" stop-color="#6c3a5c"/>
      </linearGradient>
      <linearGradient id="glowFill" x1="0" y1="0" x2="1" y2="0">
        <stop offset="0" stop-color="#f3e9df"/>
        <stop offset="1" stop-color="#c6efe9"/>
      </linearGradient>
    </defs>
    <path d="M0 112 C140 118 290 80 405 5 L405 40 C290 110 140 140 0 134 Z" fill="url(#glowFill)"/>
    <path d="M0 126 C140 132 290 96 405 22 L405 420 C300 480 150 520 0 512 Z" fill="url(#heroFill)" role="img" aria-label="Photo of smiling women exercising outdoors with hand weights"/>
    <path d="M0 112 C140 118 290 80 405 5 L405 24 C290 98 140 134 0 128 Z" fill="var(--teal)"/>
    <path d="M0 508 C150 516 300 476 405 416 L405 436 C300 500 150 534 0 530 Z" fill="var(--teal)"/>
  </svg>

  <div class="brand">
    <div class="brand__mark"></div>
    <div class="brand__name">SORREL</div>
    <div class="brand__tag">HEALTH &amp; WELLNESS</div>
  </div>

  <div class="headline">
    <div class="headline__main">A DIRECT PRIMARY CARE</div>
    <div class="headline__sub">Practice Focused On A More Holistic<br>&amp; Personal Approach to Medicine</div>
  </div>

  <div class="phone">
    <span class="phone__icon"><svg width="24" height="24" viewBox="0 0 24 24"><path d="M6.6 10.8a15 15 0 0 0 6.6 6.6l2.2-2.2c.3-.3.7-.4 1-.2 1.1.4 2.3.6 3.6.6.6 0 1 .4 1 1V20c0 .6-.4 1-1 1A17 17 0 0 1 3 4c0-.6.4-1 1-1h3.5c.6 0 1 .4 1 1 0 1.3.2 2.5.6 3.6.1.3 0 .7-.2 1z" fill="var(--ink)"/></svg></span>
    (555) 214-7730
  </div>
  <div class="address">1420 W. Elm St. STE 2B Lakeview, IN 46000</div>
</article>

<article class="card card--back">
  <svg class="back-top" viewBox="0 0 405 180">
    <path d="M0 0 H405 V55 C300 120 150 150 0 150 Z" fill="var(--cream)"/>
    <path d="M0 140 C150 140 300 110 405 55 V66 C300 128 150 162 0 166 Z" fill="var(--teal)"/>
  </svg>
  <div class="back-title">
    <div class="back-title__mark"></div>
    <div>WHAT'S INCLUDED IN<br>YOUR MEMBERSHIP :</div>
  </div>

  <ul class="perks">
    <li class="perk"><span class="perk__icon"><svg width="22" height="22" viewBox="0 0 22 22"><path d="M3 11 L11 4 L19 11 V19 H3 Z" fill="none" stroke="#fff" stroke-width="2"/><path d="M11 10v6M8 13h6" stroke="#fff" stroke-width="2"/></svg></span><span>Unlimited office<br>visits with no copay</span></li>
    <li class="perk"><span class="perk__icon"><svg width="22" height="22" viewBox="0 0 22 22"><circle cx="11" cy="7" r="3.5" fill="none" stroke="#fff" stroke-width="1.8"/><path d="M4 19c1-4 4-6 7-6s6 2 7 6z" fill="none" stroke="#fff" stroke-width="1.8"/></svg></span><span>Direct communication<br>with your doctor</span></li>
    <li class="perk"><span class="perk__icon"><svg width="22" height="22" viewBox="0 0 22 22"><circle cx="11" cy="8" r="4" fill="none" stroke="#fff" stroke-width="1.8"/><path d="M3 16h5l3 2 8-3" fill="none" stroke="#fff" stroke-width="1.8"/></svg></span><span>Discounted labs,<br>imaging &amp; medications</span></li>
    <li class="perk"><span class="perk__icon"><svg width="22" height="22" viewBox="0 0 22 22"><circle cx="11" cy="11" r="8" fill="none" stroke="#fff" stroke-width="1.8"/><path d="M7 11l3 3 5-6" fill="none" stroke="#fff" stroke-width="2"/></svg></span><span>Free initial acupuncture<br>session ($250 value).</span></li>
    <li class="perk"><span class="perk__icon"><svg width="22" height="22" viewBox="0 0 22 22"><rect x="4" y="4" width="14" height="14" rx="3" fill="none" stroke="#fff" stroke-width="1.8"/><path d="M11 11l3-3" stroke="#fff" stroke-width="2"/></svg></span><span>2 Bodyscan testings<br>per year ($100 value)</span></li>
    <li class="perk"><span class="perk__icon"><svg width="22" height="22" viewBox="0 0 22 22"><circle cx="11" cy="8" r="4" fill="none" stroke="#fff" stroke-width="1.8"/><path d="M3 16h5l3 2 8-3" fill="none" stroke="#fff" stroke-width="1.8"/></svg></span><span>Discounts for supplements<br>&amp; &nbsp;health products in the clinic</span></li>
    <li class="perk"><span class="perk__icon"><svg width="22" height="22" viewBox="0 0 22 22"><circle cx="11" cy="8" r="4" fill="none" stroke="#fff" stroke-width="1.8"/><path d="M3 16h5l3 2 8-3" fill="none" stroke="#fff" stroke-width="1.8"/></svg></span><span>Discounts for iv<br>vitamin infusion therapy</span></li>
    <li class="perk"><span class="perk__icon"><svg width="22" height="22" viewBox="0 0 22 22"><circle cx="11" cy="11" r="8" fill="none" stroke="#fff" stroke-width="1.8"/><path d="M7 11l3 3 5-6" fill="none" stroke="#fff" stroke-width="2"/></svg></span><span>Personalized nutrition<br>plan after advanced &nbsp;testing<br>such as gut microbiome,<br>hormonal, metabolism test, etc.</span></li>
  </ul>

  <div class="phone">
    <span class="phone__icon"><svg width="24" height="24" viewBox="0 0 24 24"><path d="M6.6 10.8a15 15 0 0 0 6.6 6.6l2.2-2.2c.3-.3.7-.4 1-.2 1.1.4 2.3.6 3.6.6.6 0 1 .4 1 1V20c0 .6-.4 1-1 1A17 17 0 0 1 3 4c0-.6.4-1 1-1h3.5c.6 0 1 .4 1 1 0 1.3.2 2.5.6 3.6.1.3 0 .7-.2 1z" fill="var(--ink)"/></svg></span>
    (555) 214-7730
  </div>
  <div class="website">WWW.<strong>SORREL</strong>.COM</div>
</article>

</body>
</html>
```